Landscape Contractor in need of New Web Design

HELP.. Please Help!!!!. Our current website is old, outdated, ugly... and well nothing like us.... so we are looking for someone to help build a new website that fits our company direction. We are a landscape company with multiple locations in order to meet the needs of our clients and their projects throughout the midwest. When most people think of landscaping, they think of mowing grandmas yard, but that is NOT even remotely close to what we do. We are 100% a commercial landscape company meaning we complete landscape and irrigation services for large scale commercial projects. We are looking for a website to showcase our commercial talents and awesome team of people.
Updates

Address of current website is www.plovermeadowco.com

```html
<!DOCTYPE html>
<html lang="en">
<head>
<meta charset="utf-8">
<title>Plover Meadow Co. — Landscape &amp; Irrigation</title>
<link href="https://fonts.googleapis.com/css2?family=Poppins:wght@300;400;500;600;700&display=swap" rel="stylesheet">
<style>
:root{
  --lime:#bdf200;
  --lime-soft:#d7ff4a;
  --ink:#1d2418;
  --text:#555b52;
  --muted:#8a8f86;
  --white:#ffffff;
  --line:#e3e6df;
  --dark:#17200f;
}
*{box-sizing:border-box;margin:0;padding:0}
html,body{width:1200px;height:4500px;overflow:hidden}
body{font-family:'Poppins',sans-serif;color:var(--text);background:var(--white);position:relative}
.abs{position:absolute}
.btn{display:inline-block;background:var(--lime);color:var(--ink);font-weight:600;font-size:13px;letter-spacing:.5px;padding:10px 20px;border-radius:4px}

/* header */
.site-header{top:0;left:0;width:1200px;height:70px}
.nav{top:28px;font-size:12px;color:var(--ink);display:flex;gap:24px;white-space:nowrap}
.nav-left{left:240px}
.nav-left .active{border-bottom:2px solid var(--lime);padding-bottom:4px}
.nav-right{left:695px}
.brand{left:518px;top:18px;display:flex;align-items:center;gap:8px;font-weight:700;font-size:16px;color:var(--ink);white-space:nowrap}
.brand-mark{width:20px;height:20px;background:var(--lime);border-radius:4px}
.header-cta{left:1016px;top:20px;font-size:12px;padding:9px 16px}

/* hero */
.hero-photo{left:60px;top:84px;width:620px;height:560px;background:linear-gradient(160deg,#c9d2c2 0%,#8ea27c 35%,#4f6b3c 70%,#2f4525 100%)}
.hero-grid{left:60px;top:84px}
.hero-kicker{left:735px;top:250px;font-size:40px;font-weight:700;color:var(--lime);line-height:1.1}
.hero-title{left:735px;top:296px;font-size:40px;font-weight:700;color:var(--ink);line-height:1.15;width:420px}
.hero-copy{left:735px;top:405px;width:360px;font-size:13px;line-height:1.6}
.hero-cta{left:735px;top:505px}
.socials{display:flex;gap:10px}
.social{width:30px;height:30px;border-radius:50%;border:1.5px solid var(--ink)}
.hero-social{left:1024px;top:650px}
.hero-social-line{left:930px;top:665px;width:80px;height:1px;background:var(--line)}

.section-title{width:1200px;text-align:center;font-size:30px;font-weight:600;color:var(--ink)}
.section-sub{width:1200px;text-align:center;font-size:13px;color:var(--muted)}

/* who we serve */
.sectors{top:930px;left:160px;width:880px;display:flex;justify-content:space-between}
.sector{width:130px;text-align:center;font-size:15px;font-weight:600;color:var(--ink)}
.sector-icon{width:76px;height:76px;border-radius:50%;border:2px solid var(--ink);margin:0 auto 16px;display:flex;align-items:center;justify-content:center}

/* about */
.about{top:1120px;left:0;width:1200px;height:390px;background:var(--lime)}
.about-title{left:110px;top:70px;font-size:30px;font-weight:700;color:var(--ink)}
.about-sub{left:110px;top:116px;font-size:15px;font-weight:500;color:var(--ink)}
.about-copy{left:110px;width:380px;font-size:12.5px;line-height:1.65;color:#2d3526}
.about-photo{width:270px;height:270px;border-radius:50%;border:6px solid var(--white)}

/* services grid */
.tile{overflow:hidden}
.tile-label{position:absolute;left:18px;bottom:14px;color:var(--white);font-size:14px;font-weight:500}
.maint-circle{position:absolute;left:20px;top:20px;width:180px;height:180px;border-radius:50%;background:var(--lime);display:flex;align-items:center;justify-content:center;font-size:18px;font-weight:600;color:var(--ink)}

/* experts */
.experts-title{top:2290px;font-size:30px;font-weight:700;line-height:1.3}
.experts-cta{left:538px;top:2388px}

/* why choose us */
.why{top:2500px;left:0;width:1200px;height:660px;background:radial-gradient(ellipse at 50% 55%,#3f5a2e 0%,#24341b 55%,#111a0b 100%)}
.why-title{top:80px;color:var(--white);font-size:30px;font-weight:600}
.why-sub{top:126px;color:#c8cec2;font-size:12px}
.why-photo{left:420px;top:165px;width:360px;height:360px;border-radius:50%;border:8px solid var(--lime);background:linear-gradient(180deg,#9fb3c6 0%,#c8d3dc 35%,#5d7a45 60%,#3c5a2b 100%)}
.feature{width:260px;color:#dfe4da;font-size:12px;line-height:1.55}
.feature h3{color:var(--lime);font-size:14px;font-weight:600;margin-bottom:6px}
.feature.left{text-align:right}
.feat-icon{width:38px;height:38px;border-radius:50%;background:var(--lime);display:flex;align-items:center;justify-content:center}

/* testimonial */
.quote-avatar{left:562px;top:3290px;width:76px;height:76px;border-radius:50%;background:linear-gradient(135deg,#d9ddd4,#a9b1a2);border:4px solid var(--white);box-shadow:0 0 0 1px var(--line)}
.quote-badge{left:530px;top:3300px;width:44px;height:44px;border-radius:50%;background:var(--lime);display:flex;align-items:center;justify-content:center}
.quote-text{left:300px;top:3395px;width:600px;text-align:center;font-size:13px;line-height:1.7}
.quote-name{left:300px;top:3508px;width:600px;text-align:center;font-size:15px;font-weight:600;color:var(--ink)}
.quote-role{left:300px;top:3532px;width:600px;text-align:center;font-size:12px;color:#8fbf00}
.arrow{top:3450px}

/* contact */
.contact{top:3600px;left:0;width:1200px;height:600px;background:linear-gradient(135deg,#c9f21a 0%,#a7d60c 40%,#b6e814 70%,#93c204 100%)}
.contact-lead{left:155px;top:318px;width:300px;font-size:13px;line-height:1.6;color:var(--ink)}
.form{left:590px;top:80px;width:440px}
.field{width:440px;height:40px;background:var(--white);border-radius:3px;margin-bottom:14px;padding:0 14px;font-size:12px;color:var(--muted);display:flex;align-items:center;justify-content:space-between}
.field.message{height:120px;align-items:flex-start;padding-top:12px}
.submit{margin-top:8px;border:1px solid var(--ink)}

/* footer */
.footer{top:4200px;left:0;width:1200px;height:300px;background:var(--white)}
.foot-brand{left:60px;top:36px;display:flex;align-items:center;gap:8px;font-weight:700;font-size:20px;color:var(--ink)}
.foot-hours{left:60px;top:78px;font-size:11px;color:var(--muted);line-height:1.6;width:170px}
.foot-social{left:60px;top:130px}
.foot-social .social{background:var(--lime);border-color:var(--lime)}
.foot-col h4{font-size:14px;font-weight:600;color:var(--ink);margin-bottom:14px;letter-spacing:.5px}
.foot-col ul{list-style:none;font-size:12px;line-height:2}
.foot-col li::before{content:"›";color:var(--lime);margin-right:6px;font-weight:700}
.foot-col p{font-size:12px;line-height:1.7;margin-bottom:8px}
.copyright{left:0;top:270px;width:1200px;text-align:center;font-size:11px;color:var(--muted)}
.foot-rule{left:60px;top:255px;width:1080px;height:1px;background:var(--line)}
</style>
</head>
<body>

<header class="site-header abs">
  <nav class="nav nav-left abs"><span class="active">Home</span><span>Products</span><span>Services</span><span>About Us</span></nav>
  <div class="brand abs"><span class="brand-mark"></span>Plover Meadow</div>
  <nav class="nav nav-right abs"><span>Gallery</span><span>Contact Us</span><span>Make A Payment</span></nav>
  <span class="btn header-cta abs">GET A QUOTE</span>
</header>

<section class="hero">
  <div class="hero-photo abs" role="img" aria-label="Photo of a landscaped commercial courtyard with lawn, hedges and water feature"></div>
  <svg class="hero-grid abs" width="620" height="560" viewBox="0 0 620 560" aria-hidden="true">
    <g stroke="#fff" stroke-width="3">
      <line x1="77" y1="0" x2="77" y2="560"/><line x1="155" y1="0" x2="155" y2="560"/><line x1="232" y1="0" x2="232" y2="560"/>
      <line x1="310" y1="0" x2="310" y2="560"/><line x1="387" y1="0" x2="387" y2="560"/><line x1="465" y1="0" x2="465" y2="560"/>
      <line x1="542" y1="0" x2="542" y2="560"/>
      <line x1="0" y1="70" x2="620" y2="70"/><line x1="0" y1="140" x2="620" y2="140"/><line x1="0" y1="210" x2="620" y2="210"/>
      <line x1="0" y1="280" x2="620" y2="280"/><line x1="0" y1="350" x2="620" y2="350"/><line x1="0" y1="420" x2="620" y2="420"/>
      <line x1="0" y1="490" x2="620" y2="490"/>
    </g>
    <g fill="#fff">
      <rect x="0" y="0" width="77" height="70"/><rect x="542" y="0" width="78" height="140"/>
      <rect x="465" y="0" width="77" height="70"/><rect x="0" y="490" width="155" height="70"/>
      <rect x="542" y="420" width="78" height="140"/><rect x="387" y="490" width="78" height="70"/>
      <rect x="542" y="210" width="78" height="70"/>
    </g>
  </svg>
  <div class="hero-kicker abs">Plover Meadow</div>
  <h1 class="hero-title abs">Landscape &amp; Irrigation</h1>
  <p class="hero-copy abs">Plover Meadow strives to set the standard for the highest quality lawn and landscape products and services and to exceed our customer's expectations every time.</p>
  <span class="btn hero-cta abs">CONTACT US</span>
  <div class="hero-social-line abs"></div>
  <div class="socials hero-social abs"><span class="social"></span><span class="social"></span><span class="social"></span></div>
</section>

<section class="services-intro">
  <h2 class="section-title abs" style="top:640px;left:0">Our Services</h2>
  <p class="section-sub abs" style="top:692px;left:0">Our company's dedication to innovative design projects combines some of the most distinguished landscape projects throughout the region.</p>
  <h2 class="section-title abs" style="top:790px;left:0">We Are</h2>
  <p class="section-sub abs" style="top:840px;left:0;padding:0 330px;line-height:1.6">Plover Meadow strives to set the standard for the highest quality lawn and landscape products and services and to exceed our customer's expectations every time.</p>
  <div class="sectors abs">
    <div class="sector"><div class="sector-icon"><svg width="40" height="40" viewBox="0 0 40 40" fill="none" stroke="#1d2418" stroke-width="2"><rect x="8" y="8" width="24" height="28"/><path d="M13 14h4M23 14h4M13 20h4M23 20h4M13 26h4M23 26h4M17 36v-6h6v6"/></svg></div>Commercial</div>
    <div class="sector"><div class="sector-icon"><svg width="40" height="40" viewBox="0 0 40 40" fill="none" stroke="#1d2418" stroke-width="2"><path d="M5 15L20 6l15 9z"/><path d="M9 17v14M16 17v14M24 17v14M31 17v14M5 34h30"/></svg></div>Government</div>
    <div class="sector"><div class="sector-icon"><svg width="40" height="40" viewBox="0 0 40 40" fill="none" stroke="#1d2418" stroke-width="2"><path d="M5 19L20 7l15 12"/><path d="M9 16v18h22V16M17 34v-9h6v9"/></svg></div>Residential</div>
    <div class="sector"><div class="sector-icon"><svg width="40" height="40" viewBox="0 0 40 40" fill="none" stroke="#1d2418" stroke-width="2"><rect x="6" y="14" width="28" height="20"/><path d="M14 14V8h12v6M11 20h4M18 20h4M25 20h4M11 27h4M25 27h4M18 34v-7h4v7"/></svg></div>Municipality</div>
    <div class="sector"><div class="sector-icon"><svg width="40" height="40" viewBox="0 0 40 40" fill="none" stroke="#1d2418" stroke-width="2"><rect x="5" y="9" width="30" height="22"/><path d="M20 9v22"/><circle cx="20" cy="20" r="5"/><path d="M5 15h5v10H5M35 15h-5v10h5"/></svg></div>Sports Fields</div>
  </div>
</section>

<section class="about abs">
  <h2 class="about-title abs">About Plover Meadow</h2>
  <p class="about-sub abs">100% A Commercial Landscape</p>
  <p class="about-copy abs" style="top:160px">Founded by two friends with a shared passion, Plover Meadow is the premier landscape maintenance and design company across the Midwest. Our dedication to innovative design projects combines some of the most distinguished landscape projects in the region.</p>
  <p class="about-copy abs" style="top:270px">Founded by two friends with a shared passion, Plover Meadow is the premier landscape maintenance and design company across the Midwest.</p>
  <div class="about-photo abs" style="left:575px;top:40px;background:linear-gradient(160deg,#dfe6e8 0%,#9fb08f 45%,#4f7237 100%)" role="img" aria-label="Photo of a modern office building with mature trees"></div>
  <div class="about-photo abs" style="left:780px;top:40px;background:linear-gradient(200deg,#e4ebee 0%,#8fa482 45%,#557a3a 100%)" role="img" aria-label="Photo of a commercial lawn with trees and walkways"></div>
</section>

<section class="services-grid">
  <div class="tile abs" style="left:120px;top:1745px;width:320px;height:220px;background:linear-gradient(135deg,#6f9a3a,#3f6a22)" role="img" aria-label="Photo of freshly mown lawn">
    <div class="maint-circle">Maintenance</div>
  </div>
  <div class="tile abs" style="left:455px;top:1745px;width:300px;height:220px;background:linear-gradient(180deg,#b9c4c9 0%,#8a9688 50%,#4d6d34 100%)" role="img" aria-label="Photo of a landscaped house front"><span class="tile-label">Landscaping</span></div>
  <div class="tile abs" style="left:770px;top:1745px;width:305px;height:220px;background:linear-gradient(180deg,#7e9f4b 0%,#5f7f35 60%,#3e5a22 100%)" role="img" aria-label="Photo of a worker spreading fertilizer"><span class="tile-label">Chemical Applications &amp; Fertilization</span></div>
  <div class="tile abs" style="left:120px;top:1995px;width:305px;height:215px;background:linear-gradient(160deg,#8fa679 0%,#4f6b35 60%,#2e421d 100%)" role="img" aria-label="Photo of sprinklers watering a lawn"><span class="tile-label">Irrigation</span></div>
  <div class="tile abs" style="left:440px;top:1995px;width:305px;height:215px;background:linear-gradient(160deg,#a29075 0%,#6d6a48 50%,#4c5f2c 100%)" role="img" aria-label="Photo of a crew laying new sod"><span class="tile-label">Sod Establishment &amp; Restoration</span></div>
  <div class="tile abs" style="left:760px;top:1995px;width:315px;height:215px;background:linear-gradient(160deg,#c2b9a8 0%,#8e8675 50%,#5a6b3e 100%)" role="img" aria-label="Photo of a stone paved patio"><span class="tile-label">Hardscaping</span></div>
</section>

<section class="experts">
  <h2 class="section-title experts-title abs" style="left:0">Our Experts Are Here To<br>Help You !</h2>
  <span class="btn experts-cta abs">GET A QUOTE</span>
</section>

<section class="why abs" role="img" aria-label="Dark background photo of a landscaped garden at dusk">
  <h2 class="section-title why-title abs" style="left:0">Why Choose Us?</h2>
  <p class="section-sub why-sub abs" style="left:0">Full service lawn and landscape contractors</p>
  <div class="why-photo abs" role="img" aria-label="Photo of a garden pavilion on a manicured lawn"></div>

  <div class="feature left abs" style="left:100px;top:240px"><h3>Specialized Company</h3>Plover Meadow strives to set the standard for the highest quality lawn and landscape products and services to exceed our customer's expectations.</div>
  <div class="feature left abs" style="left:100px;top:365px"><h3>Free Consultations</h3>We welcome knowing that Plover Meadow can offer free estimates and consultations for every property.</div>
  <div class="feature left abs" style="left:100px;top:470px"><h3>Reputable Company</h3>Commercial builders highly respect our design firm; their trust has allowed us to grow for over twenty years.</div>

  <div class="feature abs" style="left:840px;top:240px"><h3>Licensed &amp; Insurance</h3>Call our office to set up a time to meet with one of our certified professionals. They will walk your property with you.</div>
  <div class="feature abs" style="left:840px;top:365px"><h3>Dependable Services</h3>Contact our office today to schedule an appointment that meets your needs.</div>
  <div class="feature abs" style="left:840px;top:470px"><h3>Day Scheduling</h3>With 20 years of experience in the landscaping construction business, we have built a reputation for superior products and service.</div>

  <div class="feat-icon abs" style="left:420px;top:230px"><svg width="20" height="20" viewBox="0 0 20 20" fill="none" stroke="#1d2418" stroke-width="2"><path d="M4 10l4 4 8-8"/></svg></div>
  <div class="feat-icon abs" style="left:380px;top:350px"><svg width="20" height="20" viewBox="0 0 20 20" fill="none" stroke="#1d2418" stroke-width="2"><circle cx="10" cy="10" r="7"/><path d="M10 6v4l3 2"/></svg></div>
  <div class="feat-icon abs" style="left:420px;top:465px"><svg width="20" height="20" viewBox="0 0 20 20" fill="none" stroke="#1d2418" stroke-width="2"><path d="M10 2l2.4 5 5.4.6-4 3.7 1.1 5.4L10 14l-4.9 2.7 1.1-5.4-4-3.7 5.4-.6z"/></svg></div>
  <div class="feat-icon abs" style="left:742px;top:230px"><svg width="20" height="20" viewBox="0 0 20 20" fill="none" stroke="#1d2418" stroke-width="2"><path d="M10 2l7 3v5c0 4-3 7-7 8-4-1-7-4-7-8V5z"/></svg></div>
  <div class="feat-icon abs" style="left:782px;top:350px"><svg width="20" height="20" viewBox="0 0 20 20" fill="none" stroke="#1d2418" stroke-width="2"><path d="M4 10l4 4 8-8"/></svg></div>
  <div class="feat-icon abs" style="left:742px;top:465px"><svg width="20" height="20" viewBox="0 0 20 20" fill="none" stroke="#1d2418" stroke-width="2"><rect x="3" y="4" width="14" height="13"/><path d="M3 8h14M7 2v4M13 2v4"/></svg></div>
</section>

<section class="testimonial">
  <div class="quote-avatar abs" role="img" aria-label="Client portrait"></div>
  <div class="quote-badge abs"><svg width="20" height="16" viewBox="0 0 20 16" fill="#1d2418"><path d="M0 16V9C0 4 3 1 8 0v3C5 4 4 6 4 8h4v8zM11 16V9c0-5 3-8 8-9v3c-3 1-4 3-4 5h4v8z"/></svg></div>
  <p class="quote-text abs">I have been working with Plover Meadow for several years. As a building development firm I understand the importance of landscaping in our projects. Plover Meadow has provided expert landscape consultation and performance on all projects. I have had the opportunity to work with them on.</p>
  <p class="quote-name abs">Dana K. Ellery</p>
  <p class="quote-role abs">Ellery Development Group</p>
  <svg class="arrow abs" style="left:220px" width="24" height="24" viewBox="0 0 24 24" fill="none" stroke="#555b52" stroke-width="2"><path d="M15 4l-8 8 8 8"/></svg>
  <svg class="arrow abs" style="left:956px" width="24" height="24" viewBox="0 0 24 24" fill="none" stroke="#555b52" stroke-width="2"><path d="M9 4l8 8-8 8"/></svg>
</section>

<section class="contact abs" role="img" aria-label="Lime tinted photo of a commercial landscape">
  <p class="contact-lead abs">Feel free to ask a question or simply leave a comment.</p>
  <form class="form abs">
    <div class="field">Your Name *</div>
    <div class="field">Your Email *</div>
    <div class="field">Select Services <svg width="10" height="6" viewBox="0 0 10 6" fill="#8a8f86"><path d="M0 0h10L5 6z"/></svg></div>
    <div class="field message">Your Message</div>
    <span class="btn submit">SUBMIT</span>
  </form>
</section>

<footer class="footer abs">
  <div class="foot-brand abs"><span class="brand-mark"></span>Plover Meadow</div>
  <p class="foot-hours abs">Business Hours<br>Mon – Fri 8am – 5pm</p>
  <div class="socials foot-social abs"><span class="social"></span><span class="social"></span><span class="social"></span></div>

  <div class="foot-col abs" style="left:330px;top:36px">
    <h4>SITEMAP</h4>
    <ul><li>Home</li><li>Products</li><li>Services</li><li>About Us</li><li>Gallery</li><li>Contact Us</li><li>Make A Payment</li></ul>
  </div>
  <div class="foot-col abs" style="left:610px;top:36px;width:220px">
    <h4>CONTACT US</h4>
    <p>Plover Meadow Co.<br>2210 Meadow Lark Rd.<br>Fairview, WI 54400</p>
    <p>+1 555-014-2210</p>
    <p>hello@plovermeadowco.com</p>
  </div>
  <div class="foot-col abs" style="left:880px;top:36px;width:240px">
    <h4>CONTACT US</h4>
    <p>Plover Meadow Co.<br>418 Harvest Lane<br>Linden Falls, MN 55300</p>
    <p>+1 555-014-3380</p>
    <p>www.plovermeadowco.com</p>
  </div>
  <div class="foot-rule abs"></div>
  <p class="copyright abs">©2024 Plover Meadow Co. — All Rights Reserved</p>
</footer>

</body>
</html>
```